Roofing company in Toronto, Canada needs a logo design and business card design

We need a business card and logo created for our company. Our company is "KVL Roofing" which provides roofing services for commercial and residential customers. We serve customers in the Greater Toronto Area (in Canada) thus the name KVL.

We want the logo and business card to be a modern design displaying professionalism and quality in the work. We would prefer rounded corners for the business cards but are open to other ideas. The cards should be pleasant and appealing to customers.

Target Market(s)

Commercial and Residential customers

Industry/Entity Type

Roofing

Contact Information for Business Card

Logo Text

KVL Roofing

Requirements
Nice to have
• Colours that are pleasing to the eye but at the same time should stand out from other business cards. If the design can incorporate the name of KVL Roofing and the actual concept of roofing that would be nice.
Should not have
• Do not want the business cards or logo to be childish looking. Need to look professionally designed.

```html
<!DOCTYPE html>
<html lang="en">
<head>
<meta charset="utf-8">
<title>KVL Roofing — Business Card</title>
<link rel="stylesheet" href="https://fonts.googleapis.com/css2?family=Open+Sans:wght@400;600&display=swap">
<style>
  :root {
    --band-grey: #d0d1d3;
    --stage-white: #ffffff;
    --card-front: #f0f0f2;
    --brand-red: #d7382b;
    --card-back: #7c1608;
    --illustration-tone: #8b2a1b;
    --text-light: #ffffff;
  }
  html, body {
    margin: 0;
    padding: 0;
    width: 1200px;
    height: 1200px;
    overflow: hidden;
    background: var(--stage-white);
  }
  .presentation {
    display: block;
    width: 1200px;
    height: 1200px;
    font-family: "Open Sans", Arial, sans-serif;
  }
  .band { fill: var(--band-grey); }
  .card-front { fill: var(--card-front); }
  .card-back { fill: var(--card-back); }
  .illustration-area { fill: var(--illustration-tone); }
  .wordmark-front {
    fill: var(--brand-red);
    font-weight: 600;
    font-size: 58px;
  }
  .wordmark-back {
    fill: var(--text-light);
    font-weight: 600;
    font-size: 22px;
  }
  .holder-name {
    fill: var(--text-light);
    font-weight: 600;
    font-size: 38px;
  }
  .holder-role {
    fill: var(--text-light);
    font-weight: 600;
    font-size: 18px;
  }
  .contact-text {
    fill: var(--text-light);
    font-size: 16.5px;
  }
  .address-text {
    fill: var(--text-light);
    font-size: 13px;
    letter-spacing: 1.6px;
  }
  .icon-ring {
    fill: none;
    stroke: var(--text-light);
    stroke-width: 1.4;
  }
  .icon-glyph { fill: var(--text-light); }
  .icon-letter {
    fill: var(--text-light);
    font-family: Georgia, "Times New Roman", serif;
    font-size: 13px;
  }
</style>
</head>
<body>
<svg class="presentation" viewBox="0 0 1200 1200" xmlns="http://www.w3.org/2000/svg">
  <defs>
    <filter id="card-shadow" x="-10%" y="-10%" width="120%" height="130%">
      <feDropShadow dx="2" dy="4" stdDeviation="3" flood-color="#000" flood-opacity="0.18"/>
    </filter>
    <clipPath id="back-shape">
      <path d="M640 544 H1069 V849 H556 C560 790 520 740 536 680 C548 630 600 600 640 544 Z"/>
    </clipPath>
  </defs>

  <rect class="band" x="0" y="0" width="1200" height="145"/>
  <rect class="band" x="0" y="1024" width="1200" height="176"/>

  <!-- Front of card -->
  <g class="front-side">
    <path class="card-front" filter="url(#card-shadow)"
          d="M132 317 H644 C630 340 628 380 650 420 C672 460 675 510 652 535 C640 550 632 580 644 622 H132 Z"/>
    <text class="wordmark-front" x="390" y="528" text-anchor="middle">KVL Roofing</text>
  </g>

  <!-- Back of card -->
  <g class="back-side">
    <path class="card-back" filter="url(#card-shadow)"
          d="M640 544 H1069 V849 H556 C560 790 520 740 536 680 C548 630 600 600 640 544 Z"/>
    <g clip-path="url(#back-shape)">
      <path class="illustration-area" role="img" aria-label="Illustration: silhouette of a roofer hammering on a sloped roof"
            d="M520 849 C540 760 560 700 610 650 C650 612 700 600 745 612 C780 625 785 655 770 680 L800 720 L1069 640 V849 Z"/>
    </g>

    <text class="wordmark-back" x="1040" y="614" text-anchor="end">KVL Roofing</text>

    <text class="holder-name" x="612" y="692">MYname</text>
    <text class="holder-role" x="612" y="706">manager</text>

    <g class="contact-phone">
      <circle class="icon-ring" cx="625" cy="742" r="10.5"/>
      <path class="icon-glyph" d="M620 736.5 c1-1 2-1 2.6 0 l1.4 2.2 c.4.7.2 1.4-.4 1.8 l-.8.5 c.8 1.8 2.2 3.2 4 4 l.5-.8 c.4-.6 1.1-.8 1.8-.4 l2.2 1.4 c1 .6 1 1.6 0 2.6 c-1.4 1.4-3.4 1.4-5.4.2 c-2.6-1.5-4.8-3.7-6.3-6.3 c-1.2-2-1.2-4 .4-5.2 Z"/>
      <text class="contact-text" x="651" y="749">+1 905 555 0142</text>
    </g>
    <g class="contact-web">
      <circle class="icon-ring" cx="625" cy="772" r="10.5"/>
      <text class="icon-letter" x="625" y="776.5" text-anchor="middle">W</text>
      <text class="contact-text" x="651" y="778">www.kvlroofing.com</text>
    </g>

    <text class="address-text" x="632" y="837">128 Meridian Ave. Concord, On L4K 2B9, Canada</text>
  </g>
</svg>
</body>
</html>
```